Bluestone Advisory & Mgmt - Professional Business Cards

Hi!

I am a Real Estate Developer and Construction Consultant.

I have a lot of inspiration from previous designs and would be open to using the attached Designs as a starting point. I would like to see these styles incorporated into your designs.

I really need professional business card to go with it that includes my important info.

Look forward to seeing your designs!.

Target Market(s)

My Target market are building owners, lawyers, consultants.

Industry/Entity Type

Real Estate Development

Contact Information for Business Card

My Name: Dorian Pelkey
My Title: Principle
Company Name: Bluestone Advisory & Mgmt, LLC
Address: 348 West 71st Street, 9th FL New York, NY 10010
Mobile: 917.806.3971
Website: bam-hvx.example

Font styles to use
Serif
Sans Serif

Colors

Designer to choose colors to be used in the design.

Requirements
Must have
• Must incorporate the logo attached or have new that looks similar.
• Must use professional font that will be seen and judged by wealthy land owners and developers.
• Must incorporate some of the color green.
Should not have
• Photo's or pictures of people or buildings of any kind.

```html
<!DOCTYPE html>
<html lang="en">
<head>
<meta charset="utf-8">
<title>Bluestone Advisory &amp; Mgmt – Business Card</title>
<link href="https://fonts.googleapis.com/css2?family=Lato:wght@400;700&family=Raleway:wght@500;600&display=swap" rel="stylesheet">
<style>
  :root {
    --backdrop: #e9e6e1;
    --brand-green: #4fb87a;
    --card-white: #ffffff;
    --ink-light: #ffffff;
    --rule-light: rgba(255,255,255,0.6);
    --shadow: rgba(0,0,0,0.18);
  }
  * { margin: 0; padding: 0; box-sizing: border-box; }
  html, body {
    width: 1200px; height: 900px; overflow: hidden;
    background: var(--backdrop);
  }
  .canvas { position: relative; width: 1200px; height: 900px; }
  .card {
    position: absolute;
    box-shadow: 3px 3px 8px var(--shadow);
  }
  .card-front {
    left: 330px; top: 90px; width: 556px; height: 343px;
    background: var(--brand-green);
    color: var(--ink-light);
    font-family: "Lato", sans-serif;
    text-align: center;
  }
  .holder-name {
    position: absolute; left: 0; right: 0; top: 168px;
    font-family: "Raleway", sans-serif; font-weight: 600;
    font-size: 24px; line-height: 30px;
  }
  .front-inner { position: absolute; left: 0; right: 0; top: 80px; }
  .card-front .holder-name { top: 0; }
  .holder-title { position: absolute; left: 0; right: 0; top: 27px; font-size: 15px; line-height: 18px; }
  .divider {
    position: absolute; left: 201px; width: 152px; height: 1px;
    background: var(--rule-light);
  }
  .divider-top { top: 54px; }
  .divider-bottom { top: 116px; }
  .contact-block { position: absolute; left: 0; right: 0; top: 64px; font-size: 16px; line-height: 21px; }
  .address-block { position: absolute; left: 0; right: 0; top: 124px; font-size: 16px; line-height: 20px; }

  .card-back {
    left: 330px; top: 469px; width: 559px; height: 343px;
    background: var(--card-white);
    font-family: "Lato", sans-serif;
  }
  .brand-lockup {
    position: absolute; left: 0; right: 0; top: 120px;
    display: flex; align-items: center; justify-content: center; gap: 12px;
  }
  .brand-square { width: 30px; height: 30px; background: var(--brand-green); }
  .brand-name {
    color: var(--brand-green); font-weight: 700;
    font-size: 26px; line-height: 32px;
  }
  .web-band {
    position: absolute; left: 0; right: 0; bottom: 0; height: 47px;
    background: var(--brand-green); color: var(--ink-light);
    font-size: 16px; line-height: 47px; text-align: center;
  }
</style>
</head>
<body>
<main class="canvas">
  <section class="card card-front">
    <div class="front-inner" style="top:80px">
      <h1 class="holder-name" style="font-size:24px;font-weight:600">Dorian Pelkey</h1>
      <p class="holder-title">Principle</p>
      <span class="divider divider-top"></span>
      <p class="contact-block">917.806.3971<br>www.bam-hvx.example</p>
      <span class="divider divider-bottom"></span>
      <p class="address-block">Bluestone Advisory &amp; Mgmt, LLC<br>348 West 71st Street<br>9th FL New York, NY 10010</p>
    </div>
  </section>

  <section class="card card-back">
    <div class="brand-lockup">
      <span class="brand-square"></span>
      <span class="brand-name">Bluestone Advisory &amp; Mgmt</span>
    </div>
    <div class="web-band">www.bam-hvx.example</div>
  </section>
</main>
</body>
</html>
```